北海道緑野町(びばい)では2015年4月1日より、ふるさと納税(寄附金)をされた方に対して、謝礼品(特産品等)の贈呈を開始いたしますが、この謝礼品を紹介するパンフレットデザイン案を募集いたします。 ▽市の概要 緑野町は北海道中央部、札幌市からNVで34分(60km)、青葉台空港からはNVで80分(90km)のところにある、人口24,000人の市です。[http://www.city.midorino-example.jp/] 「みどり香るまち緑野」の名で知られる緑野町は、北海道内でも有数の米どころであり、アスパラやハスカップなどの「農」、焼き鳥やとりめしなどの「食」、そして世界的に著名な彫刻家、森川遼(りょう)氏の出身地であるなど「アート」の地としても知られています。 ▽パンフレットを作成する目的・概要 緑野町では2015年4月1日から、ふるさと納税(寄附金)をされた方に対する謝礼(特産品等の贈呈)を開始することとしております。 そこで今回緑野町では、ふるさと納税の謝礼品(特産品等)を掲載したパンフレットデザインを募集します。 ====================================================== (ふるさと納税とは?) ふるさと納税とは、個人が都道府県・市区町村へ2,000円を超える寄附を行ったときに、住民税のおよそ1割程度が所得税と住民税からそれぞれ直接還付、控除される制度です。2015年4月からは、これまで住民税の1割となっていた控除額の上限が2割に引き上げられるのに加え、寄付先の自治体は出身地にこだわらず、どの自治体でも5つまであれば確定申告が不要になるなど、制度の拡充が図られる予定です。 ====================================================== ▽具体的なご依頼内容(A4/全4ページ[A3見開き]) *以下の内容に、必要に応じてキャッチコピー等の文言や、独自の写真等を追加していただいても構いません。 【パンフレットの構成は以下の通り】 (1ページ目-表紙・寄附金の使いみちの紹介)*以下の5項目を自由にレイアウトしてください。 ①見出し 「まごころ緑野支援寄附金(ふるさと納税) 謝礼品のご案内」 ②キャッチフレーズ 「みどり香るまち緑野」 ③市の所在がわかるマップ(札幌市・青葉台空港からのアクセス) ④連絡先・お問い合わせ先 「北海道緑野町産業部 地域振興課 電話番号 メールアドレス」 (デザイン採用者が決まりましたらご連絡いたします。) ⑤寄附金の使途 「寄附金の使途は、以下の8項目から選択できます。 1 広くまちづくりへの応援をします。 2 福祉事業を応援します。~「福祉基金」 3 青少年育成事業を応援します。~「青少年育成基金」 4 文化振興事業を応援します。~「文化基金」 5 ルーチェガルテン緑野整備事業を応援します。~「ルーチェガルテン緑野整備基金」 6 交流拠点施設整備事業(ほのかの湯さらさ館ほか)を応援します。~「交流拠点施設整備基金」 7 農業振興事業を応援します。~「農業振興基金」 8 上記以外について応援します。 *緑野町では、子宮頸がんワクチン接種後に副作用を訴える人を対象とした、市独自の支援策を2015年1月から実施しています。 この市独自の支援策に活用してほしい方は、「8 上記以外について応援します。」に記載してください。」 (2~4ページ目-特産品等の紹介)*謝礼品は添付ファイルを参照してください。 ・謝礼品は、全25種類あります。 ・謝礼品をわかりやすい区分(寄付金額・商品ジャンルなど)で整理し、添付の写真を用いてレイアウトしてください。 ・1ページあたりの掲載品数に制限はありません、また写真を加工しても構いません。 利用される方が分かりやすいレイアウトでお願いします。 ・写真、文字は後日差し替える場合がございます。 ・各謝礼品に掲載する情報は、以下のとおり ①商品名(例:ハスカップ(冷凍)) ②内容・量(例:500g×3個) ③発送時期(例:通年※発送は7月以降) ④寄付金額(例:10,000円以上) ⑤商品の特徴+提供元 (例:道内屈指の米どころの緑野から…お届けします。[NK◯◯]) ・残りの写真は揃い次第、UPいたします。大変ご迷惑をお掛けしますが、よろしくお願い致します。 【パンフレット作成に使用するツール】 Adobe Photoshop / Adobe Illustrator 他 納品ファイルは、ai形式(アウトライン有/無)およびpdf形式をそれぞれご用意願います。 ▽重要視する点・経験 ・カタログ等パンフレットデザインの経験 ・コンセプトにそったパンフレットデザインを提案していただける方 ・コミュニケーションに慣れており、細かい修正などにも対応していただける方 ・本件をきっかけに、緑野町に愛着を持っていただける方 ▽注意点・禁止事項 ※他で登録されているデザインや商標の転用など、他社の知的財産権、著作権を侵すこと ※他のクライアントへ既に提案した内容の転用など ▽その他コメント 作成するパンフレットのデザインについてご質問等ありましたら、お気軽にご連絡ください。 皆様からたくさんのご応募を、心よりお待ち申し上げております! |
今回は、緑野町が27年4月からふるさと納税寄附金に対する謝礼品を開始することに伴い、緑野の地名と緑野の特産品を多くの方々に知ってもらえるデザインを期待して、ハンドメイトネットでアイデアを募集しました。
このような考え方の中、緑野の取組の見やすさ、商品写真や説明内容の見やすさなどを重点ポイントとして、皆様から提案いただいたデザインを関係者の中で検討した結果、今回のデザインを採用することといたしました。
まずは、ご提案いただきました皆様にお礼申し上げます。
予想以上に多くの方々にご提案をいただきましたことは、本当にうれしく思っております。
今回初めてハンドメイトネットを利用させていただきましたが、準備が不十分で、当初写真が揃わなかったり、内容の差し替えなどがあったことから、デザイナーの皆様には大変ご苦労をかけたこと、ご容赦いただきますよう、お願い申し上げます。
また今後もデザイナーの皆様にアイデアを募りたいときには、利用させていただきたいと思いますので、よろしくお願いいたします。
なお、パンフレットの募集の際にもお知らせをしましたが、平成27年4月1日から、緑野に対するふるさと納税による寄附をされた市外の方々に対して謝礼品の贈呈を開始いたします。詳細につきましては、3月下旬に緑野町のHPなどにおいてお知らせをさせていただきますが、もし緑野を応援したい、と思っていただける方がいらっしゃいましたら、ぜひ市までご連絡いただきますよう、お願い申し上げます。
最後になりますが、ご提案いただきましたデザイナーの皆様におかれましては、ご協力をいただき、本当にありがとうございました。

```html
<!DOCTYPE html>
<html lang="ja">
<head>
<meta charset="utf-8">
<title>まごころ緑野支援寄附金 謝礼品のご案内</title>
<link href="https://fonts.googleapis.com/css2?family=M+PLUS+Rounded+1c:wght@500;800&family=Noto+Sans+JP:wght@400;700&display=swap" rel="stylesheet">
<style>
:root{
  --purple:#8b3f8f;
  --purple-soft:#c9a6cc;
  --green:#5c9e3c;
  --green-dark:#3f7d2b;
  --teal:#3a8fb7;
  --cream:#faf6ea;
  --paper:#ffffff;
  --ink:#3b3b3b;
  --muted:#7a7a7a;
  --tag:#d9435a;
  --panel:#fdf7dc;
  --line:#e2dccb;
}
*{box-sizing:border-box;margin:0;padding:0}
html,body{width:835px;height:1200px;overflow:hidden;background:#eeeeee}
body{font-family:"Noto Sans JP",sans-serif;color:var(--ink);position:relative}
.spread{position:absolute;left:0;width:835px;background:var(--paper);display:flex}
.spread--cover{top:0;height:590px}
.spread--catalog{top:605px;height:595px;display:block}

.cover{width:418px;height:100%;background:var(--cream);position:relative;padding:14px 18px;border-right:1px solid var(--line)}
.brand{display:flex;align-items:center;gap:6px;font-size:10px;color:var(--purple);font-weight:700}
.brand-dot{width:12px;height:12px;border-radius:50%;background:var(--purple)}
.cover-title{font-family:"M PLUS Rounded 1c",sans-serif;margin-top:78px;margin-left:40px;line-height:1.15}
.cover-title .sm,.cover-title .lg{display:block;font-size:30px;color:var(--purple);font-weight:800}
.cover-title .sub{display:block;font-size:26px;color:var(--green-dark);font-weight:800;margin-top:4px}
.cover-title .note{font-size:9px;color:var(--muted);font-weight:500}
.mascot{position:absolute;right:30px;top:188px;width:110px;height:120px;border-radius:14px;background:linear-gradient(160deg,#e6d8c4,#c9a98a)}
.mascot-caption{position:absolute;right:40px;top:312px;font-size:7px;color:var(--muted);text-align:center}
.uses{position:absolute;left:40px;right:30px;top:340px;border:2px solid var(--purple-soft);border-radius:8px;background:#fff;padding:10px 12px}
.uses h2{font-size:9px;color:var(--purple);margin-bottom:6px}
.uses ol{list-style:none;font-size:8px;line-height:1.75}
.uses li span{display:inline-block;width:12px;height:12px;line-height:12px;text-align:center;border-radius:50%;background:var(--purple);color:#fff;font-size:7px;margin-right:4px}
.uses .fine{font-size:6.5px;color:var(--muted);margin-top:5px;line-height:1.5}

.features{width:417px;height:100%;position:relative;background:#fff}
.feat-head{height:26px;background:var(--teal);border-bottom-left-radius:30px}
.feat-list{list-style:none;padding:6px 14px 0 18px}
.feat{display:flex;gap:10px;height:76px;border-bottom:1px dashed var(--line);padding:6px 0}
.feat-text{flex:1;font-size:7px;line-height:1.55;color:var(--muted)}
.feat-text b{display:block;font-size:9px;color:var(--green-dark);margin-bottom:3px}
.feat-photo{width:130px;border-radius:4px}
.contact{position:absolute;left:18px;right:14px;bottom:14px}
.contact-band{background:var(--green);color:#fff;font-size:8px;font-weight:700;padding:4px 10px;border-radius:12px}
.contact-body{display:flex;justify-content:space-between;align-items:flex-end;margin-top:6px;font-size:7.5px;line-height:1.6}
.phone{display:flex;align-items:center;gap:5px;font-size:22px;font-weight:700;color:var(--green-dark)}

.grid{position:absolute;inset:6px;display:grid;grid-template-columns:repeat(8,1fr);grid-template-rows:repeat(5,1fr);gap:5px}
.item{border:1px solid var(--line);border-radius:3px;padding:3px;display:flex;flex-direction:column;font-size:6px;line-height:1.35;overflow:hidden}
.item-photo{height:52px;border-radius:2px;margin-bottom:3px;flex:none}
.item-name{font-weight:700;font-size:6.5px;color:var(--ink)}
.item-meta{color:var(--muted)}
.item-price{margin-top:auto;align-self:flex-start;background:var(--tag);color:#fff;font-size:6px;padding:0 4px;border-radius:2px}
.panel{grid-column:3/7;grid-row:2/5;background:var(--panel);border-radius:4px;padding:14px 22px;position:relative}
.panel-title{font-family:"M PLUS Rounded 1c",sans-serif;font-weight:800;color:var(--purple);font-size:22px;line-height:1.2}
.panel-title em{font-style:normal;display:block;color:var(--green-dark);font-size:18px}
.map{position:absolute;left:22px;top:108px;width:130px;height:150px;border-radius:6px;background:linear-gradient(160deg,#cfe6c2,#9cc98a)}
.access{position:absolute;left:168px;top:112px;right:18px;font-size:7px;line-height:1.6;color:var(--ink)}
.access p{margin-bottom:6px}
.gutter{position:absolute;left:417px;top:0;bottom:0;width:1px;background:var(--line)}
</style>
</head>
<body>

<section class="spread spread--cover">
  <div class="cover">
    <div class="brand"><span class="brand-dot"></span>みどり香るまち緑野</div>
    <h1 class="cover-title">
      <span class="sm">まごころ緑野</span>
      <span class="lg">支援寄附金<span class="note">（ふるさと納税）</span></span>
      <span class="sub">謝礼品のご案内</span>
    </h1>
    <div class="mascot" role="img" aria-label="町のマスコットキャラクターのイラスト"></div>
    <p class="mascot-caption">緑野町のマスコット<br>みどりちゃん</p>
    <div class="uses">
      <h2>寄附金の使途は、以下の8項目から選択できます。</h2>
      <ol>
        <li><span>1</span>広くまちづくりへの応援をします。</li>
        <li><span>2</span>福祉事業を応援します。～「福祉基金」</li>
        <li><span>3</span>青少年育成事業を応援します。～「青少年育成基金」</li>
        <li><span>4</span>文化振興事業を応援します。～「文化基金」</li>
        <li><span>5</span>ルーチェガルテン緑野整備事業を応援します。</li>
        <li><span>6</span>交流拠点施設整備事業（ほのかの湯さらさ館ほか）を応援します。</li>
        <li><span>7</span>農業振興事業を応援します。～「農業振興基金」</li>
        <li><span>8</span>上記以外について応援します。</li>
      </ol>
      <p class="fine">※町独自の支援策に活用してほしい方は、「8 上記以外について応援します。」にご記載ください。</p>
    </div>
  </div>

  <div class="features">
    <div class="feat-head"></div>
    <ul class="feat-list">
      <li class="feat"><div class="feat-text"><b>こころ育む教育環境</b>子どもたちがのびのびと学べる環境づくりに寄附金を活用します。</div><div class="feat-photo" role="img" aria-label="校舎と子どもたちの写真" style="background:linear-gradient(135deg,#d8c9a6,#a98b62)"></div></li>
      <li class="feat"><div class="feat-text"><b>ルーチェガルテン緑野（芝生広場）</b>彫刻家・森川遼氏の作品が点在する、緑豊かな野外美術空間です。</div><div class="feat-photo" role="img" aria-label="芝生広場と彫刻の写真" style="background:linear-gradient(135deg,#a9d18e,#5f9e48)"></div></li>
      <li class="feat"><div class="feat-text"><b>ルーチェガルテン緑野（回廊）</b>四季折々の景色とアートを楽しめる散策路を整備します。</div><div class="feat-photo" role="img" aria-label="回廊と芝生の写真" style="background:linear-gradient(135deg,#b7d99c,#6fa653)"></div></li>
      <li class="feat"><div class="feat-text"><b>まちの特産品</b>米どころ緑野の農産物と食文化を全国へ届けます。</div><div class="feat-photo" role="img" aria-label="特産品の写真" style="background:linear-gradient(135deg,#d9b48a,#8c5a34)"></div></li>
      <li class="feat"><div class="feat-text"><b>ほのかの湯さらさ館</b>交流拠点として、町内外の人が集う温泉施設を整備します。</div><div class="feat-photo" role="img" aria-label="温泉施設の写真" style="background:linear-gradient(135deg,#cdb79a,#8a6a4c)"></div></li>
    </ul>
    <div class="contact">
      <div class="contact-band">まごころ緑野支援寄附金についてのお問い合わせ</div>
      <div class="contact-body">
        <div>北海道緑野町産業部 地域振興課<br>〒000-0000 北海道緑野町中央1条1-1</div>
        <div>E-Mail: info@city.midorino-example.jp<br>http://www.city.midorino-example.jp/</div>
      </div>
      <div class="phone">
        <svg width="18" height="18" viewBox="0 0 24 24" aria-hidden="true"><path fill="currentColor" d="M6.6 10.8a15 15 0 0 0 6.6 6.6l2.2-2.2c.3-.3.7-.4 1-.2 1.1.4 2.3.6 3.6.6.6 0 1 .4 1 1V20c0 .6-.4 1-1 1A17 17 0 0 1 3 4c0-.6.4-1 1-1h3.5c.6 0 1 .4 1 1 0 1.3.2 2.5.6 3.6.1.3 0 .7-.2 1z"/></svg>
        0123-45-6789
      </div>
    </div>
  </div>
</section>

<section class="spread spread--catalog">
  <div class="grid">
    <div class="item"><div class="item-photo" role="img" aria-label="米袋の写真" style="background:linear-gradient(#efe6cf,#cdb98c)"></div><div class="item-name">緑野産 みどりの穂</div><div class="item-meta">5kg／通年</div><span class="item-price">10,000円以上</span></div>
    <div class="item"><div class="item-photo" role="img" aria-label="米袋の写真" style="background:linear-gradient(#efe6cf,#c8b07a)"></div><div class="item-name">緑野産 そよかぜ米</div><div class="item-meta">5kg／通年</div><span class="item-price">10,000円以上</span></div>
    <div class="item"><div class="item-photo" role="img" aria-label="海苔の写真" style="background:linear-gradient(#6d6a54,#2f2e22)"></div><div class="item-name">みどりのり</div><div class="item-meta">10袋／通年</div><span class="item-price">10,000円以上</span></div>
    <div class="item"><div class="item-photo" role="img" aria-label="冷凍果実の写真" style="background:linear-gradient(#8d6a8f,#4b2c52)"></div><div class="item-name">ハスカップ（冷凍）</div><div class="item-meta">500g×3個</div><span class="item-price">10,000円以上</span></div>
    <div class="item"><div class="item-photo" role="img" aria-label="焼き鳥の写真" style="background:linear-gradient(#d7a26a,#8a5428)"></div><div class="item-name">緑野やきとり</div><div class="item-meta">20本／通年</div><span class="item-price">10,000円以上</span></div>
    <div class="item"><div class="item-photo" role="img" aria-label="とりめしの写真" style="background:linear-gradient(#e2c48f,#a8773e)"></div><div class="item-name">とりめしセット</div><div class="item-meta">3合用×2</div><span class="item-price">10,000円以上</span></div>
    <div class="item"><div class="item-photo" role="img" aria-label="菓子の写真" style="background:linear-gradient(#f0dcc0,#c29a6a)"></div><div class="item-name">町の銘菓詰合せ</div><div class="item-meta">12個入</div><span class="item-price">10,000円以上</span></div>
    <div class="item"><div class="item-photo" role="img" aria-label="ジャムの写真" style="background:linear-gradient(#b5536a,#6a2236)"></div><div class="item-name">果実ジャム</div><div class="item-meta">3本セット</div><span class="item-price">10,000円以上</span></div>

    <div class="item"><div class="item-photo" role="img" aria-label="アスパラの写真" style="background:linear-gradient(#b8d68f,#5d8c36)"></div><div class="item-name">グリーンアスパラ</div><div class="item-meta">1kg／5月以降</div><span class="item-price">10,000円以上</span></div>
    <div class="item"><div class="item-photo" role="img" aria-label="米袋の写真" style="background:linear-gradient(#f2ead6,#cfbf96)"></div><div class="item-name">特別栽培米</div><div class="item-meta">10kg／通年</div><span class="item-price">20,000円以上</span></div>

    <div class="panel">
      <h2 class="panel-title">まごころ緑野<br>支援寄附金<em>謝礼品のご案内</em></h2>
      <div class="map" role="img" aria-label="北海道の地図と緑野町の位置"></div>
      <div class="access">
        <p>札幌市からNVで34分（60km）、青葉台空港からはNVで80分（90km）。</p>
        <p>人口24,000人、道内有数の米どころであり、「農」「食」「アート」のまちとして知られています。</p>
        <p>寄附をいただいた方へ、まちの特産品を心を込めてお届けします。</p>
      </div>
    </div>

    <div class="item"><div class="item-photo" role="img" aria-label="漬物の写真" style="background:linear-gradient(#e6d59a,#a98f3c)"></div><div class="item-name">手づくり漬物</div><div class="item-meta">4種セット</div><span class="item-price">10,000円以上</span></div>
    <div class="item"><div class="item-photo" role="img" aria-label="蕎麦の写真" style="background:linear-gradient(#c9b89a,#7d6a4d)"></div><div class="item-name">緑野そば</div><div class="item-meta">乾麺10束</div><span class="item-price">10,000円以上</span></div>
    <div class="item"><div class="item-photo" role="img" aria-label="メロンの写真" style="background:linear-gradient(#d6e3a3,#8aa53c)"></div><div class="item-name">赤肉メロン</div><div class="item-meta">2玉／7月以降</div><span class="item-price">10,000円以上</span></div>
    <div class="item"><div class="item-photo" role="img" aria-label="味噌の写真" style="background:linear-gradient(#c48a52,#7a4b22)"></div><div class="item-name">手前味噌</div><div class="item-meta">1kg×2</div><span class="item-price">10,000円以上</span></div>
    <div class="item"><div class="item-photo" role="img" aria-label="かぼちゃの写真" style="background:linear-gradient(#8fa36a,#4a5c2e)"></div><div class="item-name">ほくほくかぼちゃ</div><div class="item-meta">5kg／9月以降</div><span class="item-price">10,000円以上</span></div>
    <div class="item"><div class="item-photo" role="img" aria-label="玉ねぎの写真" style="background:linear-gradient(#e8c58e,#b07a3a)"></div><div class="item-name">たまねぎ</div><div class="item-meta">10kg／9月以降</div><span class="item-price">10,000円以上</span></div>
    <div class="item"><div class="item-photo" role="img" aria-label="酒瓶の写真" style="background:linear-gradient(#b9c8b6,#5f7560)"></div><div class="item-name">地酒セット</div><div class="item-meta">720ml×2本</div><span class="item-price">20,000円以上</span></div>
    <div class="item"><div class="item-photo" role="img" aria-label="ジンギスカンの写真" style="background:linear-gradient(#c77a5a,#7a3a22)"></div><div class="item-name">味付ジンギスカン</div><div class="item-meta">500g×4</div><span class="item-price">10,000円以上</span></div>

    <div class="item"><div class="item-photo" role="img" aria-label="木工品の写真" style="background:linear-gradient(#d7b48a,#8e6640)"></div><div class="item-name">木工クラフト</div><div class="item-meta">1点／受注制作</div><span class="item-price">30,000円以上</span></div>
    <div class="item"><div class="item-photo" role="img" aria-label="入浴券の写真" style="background:linear-gradient(#c9dbe6,#6f93aa)"></div><div class="item-name">温泉入浴券</div><div class="item-meta">10枚綴り</div><span class="item-price">10,000円以上</span></div>

    <div class="item"><div class="item-photo" role="img" aria-label="椅子の写真" style="background:linear-gradient(#d9c29c,#9b7a4c)"></div><div class="item-name">手づくり椅子</div><div class="item-meta">1脚／受注制作</div><span class="item-price">50,000円以上</span></div>
    <div class="item"><div class="item-photo" role="img" aria-label="宿泊施設の写真" style="background:linear-gradient(#cfd8c2,#7b8d66)"></div><div class="item-name">ペア宿泊券</div><div class="item-meta">1泊2食付</div><span class="item-price">50,000円以上</span></div>
    <div class="item"><div class="item-photo" role="img" aria-label="はちみつの写真" style="background:linear-gradient(#f0cf6a,#b7871e)"></div><div class="item-name">純粋はちみつ</div><div class="item-meta">300g×2</div><span class="item-price">10,000円以上</span></div>
    <div class="item"><div class="item-photo" role="img" aria-label="トマトジュースの写真" style="background:linear-gradient(#e07a5f,#962f22)"></div><div class="item-name">トマトジュース</div><div class="item-meta">6本入</div><span class="item-price">10,000円以上</span></div>
    <div class="item"><div class="item-photo" role="img" aria-label="花の写真" style="background:linear-gradient(#efc1cf,#b6677f)"></div><div class="item-name">季節の花束</div><div class="item-meta">1束／6月以降</div><span class="item-price">10,000円以上</span></div>
    <div class="item"><div class="item-photo" role="img" aria-label="ベンチの写真" style="background:linear-gradient(#d5bb92,#8d6a3e)"></div><div class="item-name">木製ベンチ</div><div class="item-meta">1台／受注制作</div><span class="item-price">100,000円以上</span></div>
    <div class="item"><div class="item-photo" role="img" aria-label="じゃがいもの写真" style="background:linear-gradient(#e4cf9c,#a8844a)"></div><div class="item-name">男爵いも</div><div class="item-meta">10kg／9月以降</div><span class="item-price">10,000円以上</span></div>
    <div class="item"><div class="item-photo" role="img" aria-label="牛乳の写真" style="background:linear-gradient(#f4f1e6,#c9c2a8)"></div><div class="item-name">緑野牛乳セット</div><div class="item-meta">1L×6本</div><span class="item-price">10,000円以上</span></div>
  </div>
  <div class="gutter"></div>
</section>

</body>
</html>
```